South African ISP needs Banner Ads designed

We require world-class Banner Ad design to showcase our new Capped Unshaped ADSL / Fibre product.

We need a modern, slick design that will deliver a High conversion rate.

Banners must include our Logo.

Text:

Capped Unshaped ADSL from R1 per GB!

```html
<!DOCTYPE html>
<html lang="en">
<head>
<meta charset="utf-8">
<title>Nimbusnet – Capped Unshaped ADSL Banner</title>
<link href="https://fonts.googleapis.com/css2?family=Teko:wght@400;500&display=swap" rel="stylesheet">
<style>
  :root {
    --bg-deep: #0d1517;
    --bg-mid: #2c3d40;
    --bg-mist: #6f8587;
    --band-blue: #3ea3d3;
    --brand-blue: #3b8fd0;
    --text-light: #ffffff;
  }
  * { margin: 0; padding: 0; box-sizing: border-box; }
  html, body {
    width: 1200px;
    height: 675px;
    overflow: hidden;
    background: var(--bg-deep);
  }
  .banner {
    position: relative;
    width: 1200px;
    height: 675px;
    overflow: hidden;
    font-family: "Teko", "Arial Narrow", sans-serif;
  }
  .hero-visual {
    position: absolute;
    inset: 0;
    background:
      radial-gradient(ellipse 30% 45% at 82% 45%, rgba(160,175,175,0.55), transparent 70%),
      radial-gradient(ellipse 55% 35% at 35% 75%, rgba(111,133,135,0.55), transparent 70%),
      radial-gradient(ellipse 50% 30% at 45% 20%, rgba(80,100,102,0.5), transparent 70%),
      linear-gradient(160deg, var(--bg-deep) 0%, var(--bg-mid) 50%, var(--bg-deep) 100%);
  }
  .headline-band {
    position: absolute;
    left: 0;
    top: 284px;
    width: 700px;
    height: 164px;
    background: linear-gradient(90deg, var(--band-blue) 0%, var(--band-blue) 80%, rgba(62,163,211,0) 100%);
  }
  .headline {
    position: absolute;
    left: 40px;
    top: 290px;
    color: var(--text-light);
    font-weight: 400;
    font-size: 96px;
    line-height: 76px;
    letter-spacing: 5px;
    text-transform: uppercase;
  }
  .brand {
    position: absolute;
    right: 22px;
    top: 24px;
    display: flex;
    align-items: center;
    gap: 12px;
  }
  .brand-dot {
    width: 44px;
    height: 44px;
    border-radius: 50%;
    background: var(--brand-blue);
  }
  .brand-name {
    color: var(--brand-blue);
    font-weight: 500;
    font-size: 64px;
    line-height: 1;
    padding-top: 8px;
  }
  .site-url {
    position: absolute;
    left: 16px;
    bottom: 10px;
    color: var(--text-light);
    font-size: 20px;
    letter-spacing: 1px;
    text-transform: uppercase;
  }
</style>
</head>
<body>
  <div class="banner">
    <div class="hero-visual" role="img" aria-label="Dancer in mid-leap dissolving into a cloud of dust particles against a dark teal background"></div>
    <div class="headline-band"></div>
    <h1 class="headline">Capped Unshaped<br>ADSL from R1 per GB!</h1>
    <div class="brand">
      <span class="brand-dot"></span>
      <span class="brand-name">nimbusnet</span>
    </div>
    <div class="site-url">http://nimbusnet.co.za</div>
  </div>
</body>
</html>
```